New Business Card for Innovative Tool Company

We need a new design of business card for our florida based tool manufacturing company. I will attach 2 files that we use for our logo, use whichever you feel works best for the card. Main colours are as per logo, and we can use different shades of black/white/grey for the background.

Contact Information for Business Card

Name/Jobtitle/cell
Corvalen Tools
Suite 212c
4316 Marrowdale Pkw
Orlando, FL32847
USA
name@corvaleninc.example
www.corvaleninc.example

Font styles to use
Sans Serif

Colors

Designer to choose colors to be used in the design.

Requirements
Must have
• Icons for Plazaro, Chirpet, Snapvale, Findlo & Vidstream

```html
<!DOCTYPE html>
<html lang="en">
<head>
<meta charset="utf-8">
<title>Corvalen Tools – Business Card</title>
<link rel="stylesheet" href="https://fonts.googleapis.com/css2?family=Open+Sans:wght@400;600;700&display=swap">
<style>
  :root {
    --backdrop: #999999;
    --card: #0b0a0b;
    --yellow: #f4ec2c;
    --white: #ffffff;
    --rule: #3a3a3a;
    --plazaro: #3b5998;
    --findlo: #dd4b39;
    --vidstream: #c4302b;
    --chirpet: #33ccff;
    --snapvale: #3f729b;
  }
  * { margin: 0; padding: 0; box-sizing: border-box; }
  html, body { width: 1200px; height: 900px; overflow: hidden; }
  body {
    background: var(--backdrop);
    font-family: "Open Sans", Arial, sans-serif;
    position: relative;
  }
  .card {
    position: absolute;
    background: var(--card);
    box-shadow: 3px 4px 6px rgba(0,0,0,0.35);
  }
  .card--front {
    left: 120px; top: 275px; width: 478px; height: 295px;
    border-radius: 0 52px 0 52px;
  }
  .card--back {
    left: 606px; top: 274px; width: 477px; height: 293px;
    border-radius: 52px 0 52px 0;
  }
  .abs { position: absolute; }

  /* front */
  .brand-mark {
    left: 300px; top: 57px; width: 72px; height: 72px;
    border: 1px solid var(--yellow); border-radius: 50%;
  }
  .brand-name {
    right: 29px; top: 133px;
    color: var(--yellow); font-weight: 700; font-size: 22px;
    letter-spacing: 0.5px; text-transform: uppercase;
  }
  .person-name {
    left: 28px; top: 164px;
    color: var(--yellow); font-weight: 700; font-size: 16px; letter-spacing: 0.3px;
  }
  .person-title {
    left: 28px; top: 182px;
    color: var(--white); font-size: 12.5px;
  }
  .title-rule {
    left: 146px; top: 191px; width: 302px; height: 1px; background: var(--rule);
  }
  .contact-list {
    left: 28px; top: 211px; list-style: none;
    color: var(--white); font-size: 13px; line-height: 17.5px;
  }
  .contact-list li { display: flex; align-items: center; gap: 5px; }
  .contact-list svg { width: 10px; height: 10px; fill: var(--yellow); flex: none; }
  .address {
    right: 29px; top: 211px; text-align: right;
    color: var(--white); font-size: 13px; line-height: 17.5px; font-style: normal;
  }
  .address-company { color: var(--yellow); text-transform: uppercase; }

  /* back */
  .back-mark {
    left: 179px; top: 86px; width: 120px; height: 120px;
    border: 2px solid var(--white); border-radius: 50%;
    display: flex; align-items: center; justify-content: center;
  }
  .back-mark span {
    color: var(--yellow); font-weight: 700; font-size: 12px;
    text-transform: uppercase; text-align: center; line-height: 15px;
  }
  .back-rule {
    left: 67px; top: 231px; width: 343px; height: 1px; background: var(--rule);
  }
  .social-list {
    left: 0; right: 0; top: 248px; list-style: none;
    display: flex; justify-content: center; gap: 8px;
    color: var(--white); font-size: 9px;
  }
  .social-list li { display: flex; align-items: center; gap: 3px; }
  .social-list i { width: 8px; height: 8px; border-radius: 50%; display: block; }
</style>
</head>
<body>
  <section class="card card--front">
    <div class="abs brand-mark"></div>
    <div class="abs brand-name">Corvalen Tools</div>

    <div class="abs person-name">DORIAN KETTLEBY</div>
    <div class="abs person-title">Managing Director</div>
    <div class="abs title-rule"></div>

    <ul class="abs contact-list">
      <li><svg viewBox="0 0 10 10"><path d="M2.5 0h5a1 1 0 0 1 1 1v8a1 1 0 0 1-1 1h-5a1 1 0 0 1-1-1V1a1 1 0 0 1 1-1zm0 1.5v6h5v-6z"/></svg>555 0142 0199</li>
      <li><svg viewBox="0 0 10 10"><path d="M0 2h10v6H0z M0 2l5 3.5L10 2" stroke="#0b0a0b" stroke-width="0.8"/></svg>name@corvaleninc.example</li>
      <li><svg viewBox="0 0 10 10"><circle cx="5" cy="5" r="4.8"/></svg>www.corvaleninc.example</li>
    </ul>

    <address class="abs address">
      <span class="address-company">Corvalen Tools</span><br>
      Suite 212c 4316 Marrowdale Pkw<br>
      Orlando, FL32847 USA
    </address>
  </section>

  <section class="card card--back">
    <div class="abs back-mark"><span>Corvalen<br>Tools</span></div>
    <div class="abs back-rule"></div>
    <ul class="abs social-list">
      <li><i style="background:var(--plazaro)"></i>Plazaro</li>
      <li><i style="background:var(--findlo)"></i>Findlo</li>
      <li><i style="background:var(--vidstream)"></i>Vidstream</li>
      <li><i style="background:var(--chirpet)"></i>Chirpet</li>
      <li><i style="background:var(--snapvale)"></i>Snapvale</li>
    </ul>
  </section>
</body>
</html>
```